VORTA Festival 2013 - Urban & Extreme Sports Festival

***Who we are and what we are doing***
We are organizing an urban and extreme sports festival in summer. This is our first year, and so far things are progressing nicely.
The VORTA Festival is an event that caters to not only the athletes but the general public as well.
Each of these events will have three key-elements; an exhibition, a workshop and a competition element. The aim is to not only showcase the various sports and their participants, but more importantly to give those interested, the opportunity to try something new.
We will have the following sports; BMX, Inline skate, Skateboard, Scooter. Circus Skills will also be a major feature (juggling, poi, devil sticks etc), as well as Street Art demonstrations.
There will be hog roasts and barbecues all weekend, as well as live bands and DJs.
We are expecting a broad range of ages attending, and are trying to appeal to families also. But most of the active participants will be between the ages of 15-30
***What we would like***
We are looking for a website template that we can then fill out with all the information ourselves.
The website must have a clean, fresh, summery, urban feel.
We will need to following buttons along the top,
About / Schedule / Partners / Media / Registration / Venue / Contact
We would also like the dates to be clear (24th 25th 26th August 2013) somewhere.
And we would like to say a huge thank you in advance to all the designers.
Looking forward to seeing what you all come up with.
Any questions please get in touch and we will do our best to answer as soon as possible!
Gareth.
Target Market(s)
Young active adventurous sporty urban cool people
Industry/Entity Type
Festival
Look and feel
Each slider illustrates characteristics of the customer's brand and the style your logo design should communicate.

```html
<!DOCTYPE html>
<html lang="en">
<head>
<meta charset="utf-8">
<title>VORTA Urban Sports Festival</title>
<link href="https://fonts.googleapis.com/css2?family=Oswald:wght@500;600&family=PT+Sans:wght@400;700&display=swap" rel="stylesheet">
<style>
:root{
  --orange:#ef6a1f;
  --orange-deep:#e5501c;
  --red-head:#d9461a;
  --ink:#2b2b2b;
  --muted:#666;
  --line:#d6d6d6;
  --page:#ebebeb;
  --white:#fff;
  --footer:#050505;
  --link:#3b5998;
}
*{box-sizing:border-box;margin:0;padding:0}
html,body{width:929px;height:1200px;overflow:hidden}
body{position:relative;background:var(--page);font-family:"PT Sans",Arial,sans-serif;color:var(--ink)}
.abs{position:absolute}

/* header */
.site-header{left:0;top:0;width:929px;height:122px;background:linear-gradient(#ececec,#fff)}
.brand{left:106px;top:4px;color:var(--orange);font-family:"Oswald",Impact,sans-serif;font-weight:600;line-height:1}
.brand-name{display:block;font-size:62px;letter-spacing:1px}
.brand-sub{display:block;font-size:30px;margin-top:4px;letter-spacing:0}
.search{left:576px;top:11px;width:231px;height:18px;display:flex;box-shadow:0 2px 3px rgba(0,0,0,.15)}
.search-input{flex:1;border:1px solid #ccc;background:#fff;font-size:10px;color:#999;padding:2px 6px;line-height:12px}
.search-btn{width:49px;background:var(--orange);color:#fff;font-size:9px;text-align:center;line-height:18px}
.account{top:50px;font-size:9px;color:var(--ink);display:flex;align-items:center;gap:5px}
.nav{left:416px;top:79px;display:flex;align-items:center;height:40px;font-size:10.5px}
.nav a{color:var(--ink);text-decoration:none;padding:0 6px;height:40px;line-height:40px;border-left:1px solid #e2e2e2}
.nav a:nth-child(2){border-left:0;margin-left:3px}
.nav .active{background:var(--orange);color:#fff;height:24px;line-height:24px;border-radius:2px;width:60px;text-align:center;border:0;padding:0}

/* hero */
.hero{left:0;top:122px;width:929px;height:289px;background:var(--orange-deep)}
.hero-shadow{left:24px;top:408px;width:814px;height:14px;background:radial-gradient(ellipse at top,rgba(0,0,0,.45),rgba(0,0,0,0) 70%)}
.hero-photo{left:106px;top:145px;width:479px;height:244px;border:3px solid #fff;background:linear-gradient(#d6e3ee 0%,#5e7a40 45%,#b8b3ab 75%,#8d8a86 100%);box-shadow:0 1px 4px rgba(0,0,0,.3)}
.hero-dates{left:86px;top:180px;color:#fff;font-family:"Oswald",Impact,sans-serif;font-weight:600;font-size:23px;line-height:43px;transform:rotate(-20deg);transform-origin:left top;text-shadow:1px 2px 3px rgba(0,0,0,.55);white-space:nowrap}
.hero-dates span{display:block}
.hero-title{left:596px;top:186px;width:238px;color:#fff;font-size:15px;font-weight:400;border-bottom:1px solid rgba(255,255,255,.5);padding-bottom:4px}
.hero-text{left:602px;top:221px;width:236px;color:#ffe3d3;font-size:10px;line-height:16.3px}
.dots{left:695px;top:381px;display:flex;gap:6px}
.dot{width:12px;height:12px;border-radius:50%;background:#1a1a1a}
.dot.on{background:#eee}

/* games */
.games-band{left:0;top:411px;width:929px;height:207px;background:linear-gradient(#fff,#f1f1f1)}
.section-title{left:98px;top:424px;color:var(--orange);font-family:"Oswald",Impact,sans-serif;font-weight:600;font-size:24px}
.arrow{top:496px;color:#777;font-size:30px;font-family:"PT Sans",sans-serif;line-height:1}
.game{top:467px;width:173px;height:126px;border:2px solid #8a8a8a;border-radius:4px;overflow:hidden}
.game-label{position:absolute;left:0;right:0;bottom:0;height:27px;background:rgba(60,60,60,.75);color:#fff;font-family:"Oswald",sans-serif;font-weight:500;font-size:12px;line-height:27px;padding-left:22px}

/* welcome */
.panel{left:95px;top:640px;width:745px;height:339px;background:#fff;border:1px solid var(--line)}
.divider{left:599px;top:658px;width:2px;height:300px;background:linear-gradient(#fff,#ddd,#fff)}
.welcome-title{left:120px;top:658px;color:var(--red-head);font-family:"Oswald",sans-serif;font-weight:500;font-size:17px}
.welcome-text{left:122px;top:691px;width:468px;font-size:9.5px;line-height:14px}
.welcome-text p{margin-bottom:27px}
.avatar{left:616px;width:47px;height:50px;border:1px solid #999;border-radius:3px}
.comment-box{left:668px;top:679px;width:131px;height:35px;border:1px solid #bbb;font-size:9px;color:#888;padding:9px 9px}
.comment-btn{left:705px;top:722px;width:94px;height:19px;border:1px solid #bbb;border-radius:3px;background:linear-gradient(#fafafa,#ddd);font-size:9.5px;color:#555;text-align:center;line-height:17px}
.like{left:804px;top:683px;font-size:9px;color:var(--ink)}
.like-btn{left:804px;top:709px;width:32px;height:14px;background:#eceef5;border:1px solid #cad4e7;font-size:8px;color:var(--link);text-align:right;padding-right:3px;line-height:12px}
.like-btn::before{content:"";position:absolute;left:2px;top:2px;width:8px;height:8px;background:var(--link)}
.rule{left:621px;width:209px;height:1px;background:#e3e3e3}
.comment{left:674px;font-size:8.3px;line-height:14px;color:#444}
.comment .who{color:#555}
.plugin{left:633px;top:922px;font-size:8.5px;color:var(--link);display:flex;align-items:center;gap:12px}
.plugin i{width:12px;height:12px;background:var(--link);display:block;border-radius:1px}

/* partners */
.partners{left:95px;top:1005px;width:745px;height:101px;background:#fff;border:1px solid var(--line)}
.partner{top:1030px;height:50px;display:flex;align-items:center;justify-content:center;font-family:"Oswald",sans-serif;font-weight:500;font-size:15px;color:#1c1c1c;gap:6px}
.partner .mark{width:14px;height:14px;border-radius:50%;background:#1c1c1c}

/* footer */
.footer{left:0;top:1126px;width:929px;height:74px;background:var(--footer);border-top:2px solid #333}
.social{top:1151px;width:17px;height:17px;border-radius:2px}
.copyright{left:669px;top:1148px;color:#ccc;font-size:8.5px}
</style>
</head>
<body>

<header class="site-header abs"></header>
<div class="brand abs"><span class="brand-name">VORTA</span><span class="brand-sub">URBAN SPORTS FESTIVAL</span></div>

<div class="search abs"><span class="search-input">type your word here</span><span class="search-btn">SEARCH</span></div>

<div class="account abs" style="left:703px">
  <svg width="8" height="9" viewBox="0 0 8 9"><rect x="1" y="4" width="6" height="5" fill="#222"/><path d="M2 4V2.5a2 2 0 0 1 4 0V4" stroke="#222" fill="none"/></svg>Login
</div>
<div class="account abs" style="left:759px">
  <svg width="10" height="10" viewBox="0 0 10 10"><rect x="0.5" y="1.5" width="7" height="8" fill="none" stroke="#222"/><path d="M3 7l1-3 5-4 1 1-5 4z" fill="#222"/></svg>Register
</div>

<nav class="nav abs">
  <a class="active">Home</a><a>About</a><a>Schedule</a><a>Partners</a><a>Media</a><a>Registration</a><a>Venue</a><a>Contact</a>
</nav>

<section class="hero abs"></section>
<div class="hero-shadow abs"></div>
<div class="hero-photo abs" role="img" aria-label="Skateboarder performing a trick above a concrete skate park ramp with spectators and trees behind"></div>
<div class="hero-dates abs"><span>24th, 25th, 26th,</span><span>August 2013</span></div>
<h2 class="hero-title abs">LOREM IPSUM DOLOR AMET, ELIT</h2>
<p class="hero-text abs">Cum sociis natoque penatibus et magnis dis parturient montes, nascetur ridiculus mus. In iaculis facilisis massa. Etiam eu urna. Sed porta.Cum sociis natoque penatibus et magnis dis parturient montes, nascetur ridiculus mus. In iaculis facilisis massa. Etiam eu urna. Sed porta.</p>
<div class="dots abs"><span class="dot on"></span><span class="dot"></span><span class="dot"></span><span class="dot"></span></div>

<section class="games-band abs"></section>
<h2 class="section-title abs">Our Festival Games</h2>
<span class="arrow abs" style="left:74px">&#10216;</span>
<span class="arrow abs" style="left:848px">&#10217;</span>

<div class="game abs" style="left:98px;background:linear-gradient(#9fbbe0,#dfe7ef)" role="img" aria-label="BMX rider in mid-air beside a tall building"><span class="game-label">BMX GAMES</span></div>
<div class="game abs" style="left:284px;background:linear-gradient(#a99a8c,#d8d2c8)" role="img" aria-label="Inline skater grinding on a skate park ramp"><span class="game-label">INLINE SKATE</span></div>
<div class="game abs" style="left:470px;background:linear-gradient(#c9d2dc,#6d7b56 60%,#7b7d72)" role="img" aria-label="Rows of scooters parked on grass in front of apartment blocks"><span class="game-label">SCOOTER</span></div>
<div class="game abs" style="left:660px;background:linear-gradient(#8a1c4c,#b8305e 60%,#8a8c3a)" role="img" aria-label="Circus performers on a brightly lit stage"><span class="game-label">CIRCUS SKILLS</span></div>

<section class="panel abs"></section>
<div class="divider abs"></div>
<h1 class="welcome-title abs">Welcome to VORTA URBAN SPORTS FESTIVAL</h1>
<div class="welcome-text abs">
  <p>Welcome to the VORTA Urban Sports Festival website. Very soon you will be able to find everything you need to know about what we have in store. We are currently working hard to creating an event that caters to not only the athletes and players of the sports and activities that you will find at the festival but to the general public as well.</p>
  <p>This will be a multifaceted event where collectives and like minded people from each discipline will come along and showcase what it is they do best whilst encouraging the general public to watch, learn and participate.</p>
  <p>We are still busy constructing the website but in the meantime why not check out our social event page and the websites of some of our partners by clicking on their links above.</p>
  <p>If you have any questions please feel free to contact us by clicking the contact us icon.</p>
</div>

<div class="avatar abs" style="top:681px;background:linear-gradient(#a8b4bc,#7a6a4e)" role="img" aria-label="Profile photo of the commenting user"></div>
<div class="comment-box abs">Add a Comment</div>
<div class="comment-btn abs">Comment using...</div>
<div class="like abs">
  <svg width="10" height="9" viewBox="0 0 10 9"><path d="M1 4h2v5H1zM3 4l2-4c1 0 1.5 1 1 2L5.5 3.5H9v2L8 9H3z" fill="none" stroke="#3b5998"/></svg> 6
</div>
<div class="like-btn abs">Like</div>

<div class="rule abs" style="top:754px"></div>
<div class="avatar abs" style="top:767px;background:linear-gradient(#9a9a9a,#5a4a3e)" role="img" aria-label="Profile photo of commenter"></div>
<div class="comment abs" style="top:767px"><div class="who">Marcus Ellwood · Brighton</div><div>This is going to be a bit of a giggle ;).</div><div>Reply · 1 · <span style="color:#3b5998">&#9650;</span> 6 · March at 17:01</div></div>

<div class="rule abs" style="top:827px"></div>
<div class="avatar abs" style="top:845px;background:linear-gradient(#6b4a36,#c89a7e)" role="img" aria-label="Profile photo of commenter"></div>
<div class="comment abs" style="top:845px"><div class="who">Marcus Ellwood · Brighton</div><div>This is going to be a bit of a giggle ;).</div><div>Reply · 1 · <span style="color:#3b5998">&#9650;</span> 6 · March at 17:01</div></div>

<div class="rule abs" style="top:912px"></div>
<div class="plugin abs"><i></i>Social comments plugin</div>

<section class="partners abs"></section>
<div class="partner abs" style="left:120px;width:110px"><span class="mark"></span>Kerb Kings</div>
<div class="partner abs" style="left:255px;width:100px">Ollie Forge</div>
<div class="partner abs" style="left:375px;width:170px">VORTA</div>
<div class="partner abs" style="left:566px;width:96px"><span class="mark" style="border-radius:0"></span>Subgrade</div>
<div class="partner abs" style="left:686px;width:117px">Wheelhouse</div>

<footer class="footer abs"></footer>
<span class="social abs" style="left:105px;background:#3b5998"></span>
<span class="social abs" style="left:134px;background:#2aa3d6"></span>
<span class="social abs" style="left:164px;background:#1c74b3"></span>
<span class="social abs" style="left:193px;background:#f28a1e"></span>
<p class="copyright abs">© 2013 vortafestival.co.uk, All Rights Reserved</p>

</body>
</html>
```